Full service meeting planning company needs new business cards

Velmora Linkway is a full service meeting planning company that specializes in on-line conference registration web development and event communications. We combine citywide hotel management, mobile applications, eblast reminders, confirmation letters, and customized reporting to create a seamless registration process. We also manage group motor coach transportation, food and beverages, entertainment, stage and lighting for group of 10 to 4000.

Target Market(s)

Corporations and associations

Industry/Entity Type

Event Planning

Contact Information for Business Card

standard size 3.5" wide and 2" tall

Font styles to use
Serif
Sans Serif

Colors
f37122
f78f20
333333
5c5c5c
9d9d9d
f68d4d

Requirements
Must have
• {name}
• Velmora Linkway
• P.O. Box 7384, Grand Rapids, M I 49568
• www.velmoralinkway.com
• {email}
• {phone}
• {mobile phone}
Nice to have
• Our colors are black, grey and orange as an accent color
Should not have
• I am not happy with our website layout anymore either. It feels dark and old but it does explain who we are pretty well if you'd like to review; www.velmoralinkway.com

```html
<!DOCTYPE html>
<html lang="en">
<head>
<meta charset="utf-8">
<title>Velmora Linkway – Business Cards</title>
<link rel="stylesheet" href="https://fonts.googleapis.com/css2?family=Montserrat:wght@400;500;600&display=swap">
<style>
  :root {
    --orange: #f37122;
    --orange-warm: #f78f20;
    --white: #ffffff;
    --backdrop: #333333;
    --ink-soft: #5c5c5c;
  }
  * { margin: 0; padding: 0; box-sizing: border-box; }
  html, body {
    width: 1200px; height: 900px; overflow: hidden;
    background: var(--backdrop);
    font-family: "Montserrat", sans-serif;
  }
  .canvas { position: relative; width: 1200px; height: 900px; }

  .card {
    position: absolute;
    width: 560px; height: 320px;
    border-radius: 22px;
    overflow: hidden;
  }

  /* Front */
  .card-front {
    left: 60px; top: 90px;
    background: var(--white);
    display: flex; flex-direction: column; align-items: center; justify-content: center;
    gap: 22px;
  }
  .brand-dot {
    width: 118px; height: 118px; border-radius: 50%;
    background: var(--orange-warm);
  }
  .brand-name {
    color: var(--orange-warm);
    font-weight: 600; font-size: 19px; letter-spacing: 0.5px;
    text-transform: uppercase;
  }

  /* Back */
  .card-back {
    left: 580px; top: 490px;
    background: var(--orange-warm);
    color: var(--white);
  }
  .back-disc {
    position: absolute;
    left: 245px; top: -125px;
    width: 350px; height: 350px; border-radius: 50%;
    background: var(--white);
  }
  .holder {
    position: absolute; left: 34px; top: 146px;
  }
  .holder-name { font-size: 17px; font-weight: 500; letter-spacing: 0.6px; text-transform: uppercase; line-height: 21px; }
  .holder-title { font-size: 12px; font-weight: 400; margin-top: 1px; line-height: 15px; }
  .contact {
    position: absolute; left: 34px; top: 206px;
    list-style: none; font-size: 11.5px; line-height: 17px;
  }
  .contact li { display: flex; align-items: center; gap: 9px; }
  .contact .address { margin-bottom: 3px; }
  .contact svg { width: 11px; height: 11px; flex: none; }
</style>
</head>
<body>
<main class="canvas">
  <section class="card card-front" aria-label="Card front">
    <div class="brand-dot"></div>
    <div class="brand-name">Velmora Linkway</div>
  </section>

  <section class="card card-back" aria-label="Card back">
    <div class="back-disc"></div>
    <div class="holder">
      <div class="holder-name">Marcus Hale</div>
      <div class="holder-title">Visionary &amp; Founder</div>
    </div>
    <ul class="contact">
      <li class="address">P.O. Box 7384, Grand Rapids, M I 49568</li>
      <li>
        <svg viewBox="0 0 12 12" aria-hidden="true"><path fill="#fff" d="M1 4c0-2 2-3 5-3s5 1 5 3l-2 1-1-1.5H4L3 5 1 4zm2 2h6l1 5H2z"/></svg>
        1800.555.0187
      </li>
      <li>
        <svg viewBox="0 0 12 12" aria-hidden="true"><rect x="3" y="0.5" width="6" height="11" rx="1.2" fill="none" stroke="#fff"/><circle cx="6" cy="9.6" r="0.7" fill="#fff"/></svg>
        1800.555.0187
      </li>
      <li>
        <svg viewBox="0 0 12 12" aria-hidden="true"><path fill="#fff" d="M11.5 0.5 0.5 5l4 1.5L6 11.5z"/></svg>
        info@velmoralinkway.com
      </li>
      <li>
        <svg viewBox="0 0 12 12" aria-hidden="true"><circle cx="6" cy="6" r="5" fill="none" stroke="#fff"/><ellipse cx="6" cy="6" rx="2.2" ry="5" fill="none" stroke="#fff" stroke-width="0.8"/><path d="M1 6h10" stroke="#fff" stroke-width="0.8"/></svg>
        www.velmoralinkway.com
      </li>
    </ul>
  </section>
</main>
</body>
</html>
```